Creative - Appealing - Business Card Design Project

Looking for a Business card design (vector artwork) for an existing company called 'Fernway Sound'. We operate in the entertainment industry specializing in audio system design and rental, however; we also deal with other sectors of the entertainment industry including lighting, video, staging and power system design and rental. We would like to see designs that don't focus too much on audio but include elements encompassing everything else.

Double sided business card, following our new colour scheme and logo, which is attached. The card would ideally be creative and eye catching to draw in new customers in the elegant event production market, such as weddings & corporate affairs.

Target Market(s)

High end corporate clients, wedding clients

Industry/Entity Type

Entertainment

Requirements
Must have
• Our contact details, these can be worded & listed however you think appropriate as part as the design

Business Name - Fernway Sound
My Name - Dominic Harwell
Web Address - www.fernwaysound-example.com
Mobile Number - 07914 362 517
Office Number - 0330 481 7265
Email - dom@fernwaysound-example.com

The name, email and mobile number would need to be able to be changed to my business partners also.

The font used on our logo is Sansation
Nice to have
• On one side maybe a word cloud involving the services in which we can provide; Lighting, Sound, Event Production, Staging, LED Uplighting, Projection Mapping, Wedding Hire

On the other side, all the important credentials of contact.
Should not have
• The design should not use any old style fonts (i.e Times New Roman, Gothic etc) or on the other side of the scale, any 'jokey' fonts (i.e. Comic Sans).

The font to be used is Sansation

```html
<!DOCTYPE html>
<html lang="en">
<head>
<meta charset="utf-8">
<title>Fernway Sound – Business Card</title>
<link rel="stylesheet" href="https://fonts.googleapis.com/css2?family=Alegreya+Sans:wght@400;500;700&display=swap">
<style>
  :root {
    --backdrop: #a08e84;
    --card-grey: #c0c1c3;
    --purple: #5a3f8e;
    --purple-deep: #473177;
    --ink: #111111;
    --white: #ffffff;
    --dot: #3a3a3a;
  }
  * { box-sizing: border-box; margin: 0; padding: 0; }
  html, body { width: 1200px; height: 1009px; overflow: hidden; }
  body {
    background: var(--backdrop);
    font-family: "Alegreya Sans", sans-serif;
    position: relative;
  }
  .card {
    position: absolute;
    width: 600px;
    height: 340px;
    background: var(--card-grey);
    overflow: hidden;
    box-shadow: 6px 8px 14px rgba(0,0,0,0.35);
  }
  .card--front { left: 160px; top: 125px; }
  .card--back { left: 470px; top: 560px; }

  .card__art { position: absolute; inset: 0; width: 100%; height: 100%; }

  /* front */
  .brand {
    position: absolute;
    left: 22px; top: 30px;
    width: 230px;
    display: flex; flex-direction: column; align-items: center; gap: 14px;
  }
  .brand__dot {
    width: 96px; height: 96px; border-radius: 50%;
    background: var(--purple);
  }
  .brand__name {
    font-size: 30px; font-weight: 700; color: var(--purple);
    line-height: 1; white-space: nowrap;
  }
  .holder { position: absolute; left: 10px; top: 268px; }
  .holder__name { font-size: 27px; font-weight: 500; color: var(--purple); line-height: 1.1; white-space: nowrap; }
  .holder__company { font-size: 18px; color: var(--ink); margin-left: 6px; margin-top: 4px; }

  .contacts {
    position: absolute; left: 276px; top: 212px;
    display: grid; grid-template-columns: auto 1fr; column-gap: 6px; row-gap: 2px;
    color: var(--white); font-size: 18px;
  }
  .contacts dt { font-weight: 700; text-align: right; }
  .contacts dd { white-space: nowrap; }

  /* back */
  .mark {
    position: absolute; left: 240px; top: 55px;
    width: 120px; height: 120px; border-radius: 50%;
    background: var(--purple);
  }
  .back__title {
    position: absolute; left: 0; right: 0; top: 190px;
    text-align: center; font-size: 30px; font-weight: 500; color: var(--purple-deep);
  }
  .services {
    position: absolute; left: 190px; top: 238px;
    list-style: none; color: var(--white); font-size: 19px; line-height: 1.45;
  }
  .services li::before {
    content: ""; display: inline-block; width: 7px; height: 7px; border-radius: 50%;
    background: var(--dot); margin-right: 7px; vertical-align: middle;
  }
</style>
</head>
<body>

<section class="card card--front" aria-label="Business card front">
  <svg class="card__art" viewBox="0 0 600 340" aria-hidden="true">
    <defs>
      <linearGradient id="panelFront" x1="0" x2="1" y1="0" y2="0">
        <stop offset="0" stop-color="#5d4290"/>
        <stop offset="0.4" stop-color="#6a4f9a"/>
        <stop offset="1" stop-color="#4e3785"/>
      </linearGradient>
    </defs>
    <polygon points="270,155 580,0 600,0 600,340 270,340" fill="url(#panelFront)"/>
    <polygon points="270,132 535,0 585,0 270,158" fill="#ffffff" opacity="0.18"/>
    <polygon points="270,158 585,0 600,0 600,8 270,174" fill="#ffffff" opacity="0.1"/>
  </svg>

  <div class="brand">
    <span class="brand__dot"></span>
    <span class="brand__name">Fernway Sound</span>
  </div>

  <div class="holder">
    <p class="holder__name">Dominic Harwell</p>
    <p class="holder__company">Fernway Sound</p>
  </div>

  <dl class="contacts">
    <dt>Mobile :</dt><dd>07914 362 517</dd>
    <dt>Office :</dt><dd>0330 481 7265</dd>
    <dt>Email :</dt><dd>dom@fernwaysound-example.com</dd>
    <dt>Web :</dt><dd>www.fernwaysound-example.com</dd>
  </dl>
</section>

<section class="card card--back" aria-label="Business card back">
  <svg class="card__art" viewBox="0 0 600 340" aria-hidden="true">
    <defs>
      <linearGradient id="bandBack" x1="0" x2="0" y1="0" y2="1">
        <stop offset="0" stop-color="#8a78b4"/>
        <stop offset="0.25" stop-color="#644a98"/>
        <stop offset="1" stop-color="#3f2b6c"/>
      </linearGradient>
    </defs>
    <rect x="0" y="198" width="600" height="142" fill="url(#bandBack)"/>
  </svg>

  <span class="mark"></span>
  <h2 class="back__title">Fernway Sound</h2>
  <ul class="services">
    <li>Lighting, Sound, Event Production</li>
    <li>Staging, LED Uplighting</li>
    <li>Projection Mapping, Wedding Hire</li>
  </ul>
</section>

</body>
</html>
```